RESIDENTIAL CONSTRUCTION

We are a company that specializes in building custom residential homes, the design should also emphasize that quality and service is our priority.

Industry/Entity Type

Construction Company

Contact Information for Business Card

Contact Person: Tobias Kerrigan
Company Address: 243 West 9th St San Jose , Ca 95387
Phone Number : 408-736-2049
Email Address: Stonegatecrafts517@mailbrook.net

Font styles to use
Sans Serif

Colors
ec1f27

Requirements
Must have
• CSLB # 2736159
Nice to have
• needs to have same color as logo i uploaded, we will be printing these on a clear plastic card.

```html
<!DOCTYPE html>
<html lang="en">
<head>
<meta charset="UTF-8">
<title>Stonegate Builders — Business Card</title>
<link href="https://fonts.googleapis.com/css2?family=Oswald:wght@500;600&family=Open+Sans:wght@400&display=swap" rel="stylesheet">
<style>
  :root {
    --backdrop: #1c1c1e;
    --card: #1e1e20;
    --card-edge: #2a2a2c;
    --red: #ec1f27;
    --white: #f2f2f2;
    --body-text: #e4e4e4;
    --emboss: #141416;
  }
  * { margin: 0; padding: 0; box-sizing: border-box; }
  html, body {
    width: 1200px; height: 900px; overflow: hidden;
    background: var(--backdrop);
  }
  .canvas {
    position: relative; width: 1200px; height: 900px;
  }
  .card {
    position: absolute; left: 250px; width: 700px; height: 400px;
    background: var(--card);
    border: 1px solid var(--card-edge);
    box-shadow: 0 10px 30px rgba(0,0,0,.45);
  }
  .card--front { top: 40px; }
  .card--back { top: 470px; }

  .brand {
    display: flex; align-items: center; gap: 14px;
    font-family: 'Oswald', sans-serif; font-weight: 600;
    text-transform: uppercase; letter-spacing: 1px; line-height: 1;
  }
  .brand__square { width: 14px; height: 14px; }

  .card--front .brand {
    position: absolute; left: 0; right: 0; top: 0; bottom: 0;
    justify-content: center; font-size: 58px; color: var(--emboss);
  }
  .card--front .brand__square { background: var(--emboss); width: 22px; height: 22px; }

  .holder {
    position: absolute; left: 60px; top: 50px;
  }
  .holder__name {
    font-family: 'Oswald', sans-serif; font-weight: 600;
    font-size: 30px; color: var(--white); text-transform: uppercase;
    letter-spacing: .5px; line-height: 1.1;
  }
  .holder__title {
    font-family: 'Oswald', sans-serif; font-weight: 500;
    font-size: 17px; color: var(--red); text-transform: uppercase;
    margin-top: 2px;
  }
  .holder__rule {
    width: 72px; height: 3px; background: var(--red); margin-top: 10px;
  }

  .card--back .brand {
    position: absolute; right: 50px; top: 125px;
    font-size: 38px; color: var(--red);
  }
  .card--back .brand__square { background: var(--red); }

  .contact {
    position: absolute; left: 60px; bottom: 56px;
    list-style: none;
    font-family: 'Open Sans', sans-serif; font-size: 18px; color: var(--body-text);
  }
  .contact__item { display: flex; align-items: center; gap: 14px; height: 30px; }
  .contact__icon { width: 16px; height: 16px; fill: var(--red); flex: none; }
</style>
</head>
<body>
<main class="canvas">
  <section class="card card--front" aria-label="Card front">
    <div class="brand"><span class="brand__square"></span>Stonegate Builders</div>
  </section>

  <section class="card card--back" aria-label="Card back">
    <div class="holder">
      <h1 class="holder__name">Tobias Kerrigan</h1>
      <p class="holder__title">Job Title | CSLB # 2736159</p>
      <div class="holder__rule"></div>
    </div>

    <div class="brand"><span class="brand__square"></span>Stonegate Builders</div>

    <ul class="contact">
      <li class="contact__item">
        <svg class="contact__icon" viewBox="0 0 24 24" aria-hidden="true"><path d="M6.6 10.8a15.1 15.1 0 0 0 6.6 6.6l2.2-2.2a1 1 0 0 1 1-.25 11.4 11.4 0 0 0 3.6.57 1 1 0 0 1 1 1V20a1 1 0 0 1-1 1A17 17 0 0 1 3 4a1 1 0 0 1 1-1h3.5a1 1 0 0 1 1 1c0 1.25.2 2.45.57 3.57a1 1 0 0 1-.25 1z"/></svg>
        408-736-2049
      </li>
      <li class="contact__item">
        <svg class="contact__icon" viewBox="0 0 24 24" aria-hidden="true"><path d="M2 5h20v14H2z M2 5l10 8 10-8" /><path d="M3 6l9 7 9-7v-.5H3z" fill="#1e1e20"/></svg>
        Stonegatecrafts517@mailbrook.net
      </li>
      <li class="contact__item">
        <svg class="contact__icon" viewBox="0 0 24 24" aria-hidden="true"><path d="M12 2a7 7 0 0 0-7 7c0 5.2 7 13 7 13s7-7.8 7-13a7 7 0 0 0-7-7zm0 9.5A2.5 2.5 0 1 1 12 6.5a2.5 2.5 0 0 1 0 5z"/></svg>
        243 West 9th St San Jose , Ca 95387
      </li>
    </ul>
  </section>
</main>
</body>
</html>
```